Innovative Healthcare Technology Company needs a Business Card Design

We are in need of an innovative business card design for a new healthcare software company called "Lumenwise Data Partners". We develop software that creates medical assessment applications and mobile e-learning prevention services to reduce risk behaviors in adolescent and young adults. Our initial product, the "KESTREL App", conducts a tailored sexual risk assessment and provides a doctor with an insightful patient report to improve sexual risk counseling and ultimately reduce unintended pregnancy, STDs, etc.

We would like the design to incorporate our logo and branding colors (attached) in an innovative and creative manner. The final design should communicate professionalism and healthcare innovation. Our tag line is "prevention is the solution" (doesn't necessarily need to be included) and our target audience is doctors, medical directors, and medical business administrators. Please visit our website for additional info ourbrightmarq.com. Be creative and we look forward to seeing your designs!

Target Market(s)

healthcare - doctors, medical directors and medical business administrators

Industry/Entity Type

Healthcare

Contact Information for Business Card

We would like the design to incorporate our logo and branding colors (attached) in an innovative and creative manner. The final design should communicate professionalism and healthcare innovation. Our tag line is "prevention is the solution" (doesn't necessarily need to be included)

Font styles to use
Other font styles liked:
• quicksand

Requirements
Must have
• our logo and brand colors
• Name, (Mara Feldhovenik, PhD)
• Email (drmara@ourbrightmarq.com)
• phone (555.283.9170)
• Website (ourbrightmarq.com)
Should not have
• cartoon look

```html
<!DOCTYPE html>
<html lang="en">
<head>
<meta charset="utf-8">
<title>Lumenwise Data Partners – Business Card</title>
<link rel="stylesheet" href="https://fonts.googleapis.com/css2?family=Quicksand:wght@300;400;700&display=swap">
<style>
  :root {
    --brand-blue: #1f5bc4;
    --band-blue: #1f5dc8;
    --text-grey: #8e9a98;
    --card-white: #ffffff;
  }
  * { margin: 0; padding: 0; box-sizing: border-box; }
  html, body {
    width: 1200px;
    height: 686px;
    overflow: hidden;
    background: var(--card-white);
  }
  .card {
    position: relative;
    width: 1200px;
    height: 686px;
    background: var(--card-white);
    font-family: "Quicksand", sans-serif;
    overflow: hidden;
  }
  .brand {
    position: absolute;
    left: 71px;
    top: 100px;
    display: flex;
    align-items: center;
    gap: 20px;
  }
  .brand-square {
    width: 58px;
    height: 58px;
    background: var(--brand-blue);
  }
  .brand-name {
    font-size: 46px;
    font-weight: 400;
    color: var(--brand-blue);
    line-height: 1;
    letter-spacing: 0.5px;
  }
  .contact {
    position: absolute;
    right: 57px;
    top: 300px;
    text-align: right;
  }
  .person-name {
    font-size: 41px;
    font-weight: 700;
    color: var(--brand-blue);
    line-height: 55px;
    letter-spacing: 2px;
  }
  .contact-line {
    font-size: 44px;
    font-weight: 300;
    color: var(--text-grey);
    line-height: 58px;
    letter-spacing: 1px;
  }
  .web-band {
    position: absolute;
    left: 528px;
    top: 571px;
    right: 0;
    bottom: 0;
    background: var(--band-blue);
  }
  .web-address {
    position: absolute;
    right: 57px;
    top: 50%;
    transform: translateY(-50%);
    font-size: 38px;
    font-weight: 700;
    color: var(--card-white);
    letter-spacing: 3px;
    white-space: nowrap;
  }
</style>
</head>
<body>
  <main class="card">
    <header class="brand">
      <span class="brand-square"></span>
      <span class="brand-name">Lumenwise Data Partners</span>
    </header>

    <section class="contact">
      <p class="person-name">Mara Feldhovenik,<br>PhD</p>
      <p class="contact-line">(t) 555.283.9170</p>
      <p class="contact-line">(e)drmara@ ourbrightmarq.com</p>
    </section>

    <footer class="web-band">
      <span class="web-address">www.ourbrightmarq.com</span>
    </footer>
  </main>
</body>
</html>
```